Stationery Design Project for Lakemont Kenbu Kai Karate Studio

We Need a Stationery Design for a Karate School Teaching Okinawa Shorin Ryu Karate in Cedar Hollow, Florida, U.S.A.

Target Market(s)

Adults Base Western Speaking aged between 25 and 65 yrs, old that handle household budgets

Industry/Entity Type

School

Requirements
Must have
• Name of business: Lakemont Kenbu Kai Karate Studio
Address: Maplecrest Plaza 38214 US Hwy. 61
Cedar Hollow, Florida. 33812
Phone # : 352-555-0183
email : Lakemontkenbukaistudio@samplemail.net
Logo - attatched

```html
<!DOCTYPE html>
<html lang="en">
<head>
<meta charset="utf-8">
<title>Lakemont Kenbu Kai Karate Studio – Stationery</title>
<link rel="stylesheet" href="https://fonts.googleapis.com/css2?family=Arimo:wght@400;700&family=Open+Sans:wght@400;600;700;800&display=swap">
<style>
  :root {
    --gold: #eccb17;
    --gold-line: #e8c21a;
    --black: #000000;
    --red: #d52027;
    --grey-band: #7a7a7a;
    --ink: #1a1a1a;
    --faint: #ececec;
    --faint-red: #f6dada;
    --paper: #ffffff;
    --frame: #8a8a8a;
  }
  html, body { margin: 0; padding: 0; overflow: hidden; }
  body { width: 1200px; height: 1200px; background: var(--paper); position: relative; font-family: "Arimo", Arial, sans-serif; color: var(--ink); }
  .label { position: absolute; font-family: "Open Sans", Arial, sans-serif; font-size: 26px; color: var(--ink); text-align: center; width: 300px; margin-left: -150px; }

  /* Letterhead */
  .letterhead { position: absolute; left: 24px; top: 110px; width: 522px; height: 675px; border: 1px solid var(--frame); box-sizing: border-box; background: var(--paper); overflow: hidden; }
  .letterhead__name { position: absolute; left: 32px; top: 46px; font-size: 16px; }
  .letterhead__rule { position: absolute; left: 30px; top: 67px; width: 484px; height: 3px; background: var(--gold-line); border-radius: 2px; }
  .letterhead__contact { position: absolute; left: 36px; top: 72px; font-size: 10.5px; white-space: nowrap; display: flex; align-items: center; gap: 4px; }
  .letterhead__contact b { font-weight: 700; }
  .dot { display: inline-block; width: 9px; height: 9px; border-radius: 50%; background: var(--red); margin: 0 2px; }
  .letterhead__mark { position: absolute; left: 90px; top: 250px; width: 340px; text-align: center; }
  .letterhead__mark .ring { width: 150px; height: 150px; border-radius: 50%; background: var(--faint-red); margin: 0 auto 30px; }
  .mark-text { font-family: "Open Sans", Arial, sans-serif; font-weight: 800; color: var(--faint); font-size: 42px; line-height: 1.1; }
  .letterhead__email { position: absolute; left: 0; width: 100%; top: 623px; text-align: center; font-family: "Open Sans", Arial, sans-serif; font-weight: 600; font-size: 11px; color: var(--gold-line); }

  /* Envelope front */
  .envelope-front { position: absolute; left: 598px; top: 168px; width: 548px; height: 274px; background: var(--gold); overflow: hidden; }
  .envelope-front__band { position: absolute; left: 0; top: 0; width: 100%; height: 21px; background: var(--black); }
  .envelope-front__return { position: absolute; left: 25px; top: 25px; font-family: "Open Sans", Arial, sans-serif; font-size: 8px; line-height: 1.2; color: var(--ink); }
  .envelope-front__return .studio { color: var(--red); font-weight: 700; }
  .envelope-front__mark { position: absolute; left: 335px; top: 70px; width: 200px; text-align: center; opacity: 0.22; }
  .envelope-front__mark .ring { width: 50px; height: 50px; border-radius: 50%; background: var(--black); margin: 0 auto 14px; }
  .envelope-front__mark .mark-text { color: var(--black); font-size: 20px; }

  /* Envelope back */
  .envelope-back { position: absolute; left: 600px; top: 511px; width: 542px; height: 271px; }
  .envelope-back svg { display: block; }

  /* Business cards */
  .card { position: absolute; background: var(--gold); overflow: hidden; }
  .card--front { left: 260px; top: 916px; width: 290px; height: 192px; }
  .card--back { left: 623px; top: 916px; width: 300px; height: 190px; }
  .card__brand { position: absolute; display: flex; flex-direction: column; align-items: center; text-align: center; }
  .card__brand .ring { width: 30px; height: 30px; border-radius: 50%; background: var(--red); margin-bottom: 8px; }
  .card__brand .brand-name { font-weight: 700; font-size: 14px; line-height: 1.1; color: var(--black); }
  .card--front .card__brand { left: 14px; top: 44px; width: 110px; }
  .card--back .card__brand { left: 80px; top: 50px; width: 140px; }
  .card--back .brand-name { font-size: 16px; }
  .card__person { position: absolute; right: 26px; top: 33px; text-align: right; }
  .card__person .name { color: var(--paper); font-weight: 700; font-size: 13px; }
  .card__person .role { color: var(--red); font-weight: 700; font-style: italic; font-size: 10px; margin-top: 2px; }
  .card__address { position: absolute; right: 26px; top: 94px; text-align: right; font-size: 10px; line-height: 1.3; }
  .card__address .plaza { font-weight: 700; }
  .card__address .phone { font-weight: 700; font-size: 12px; }
  .card__email { position: absolute; left: 0; width: 100%; top: 154px; text-align: center; font-size: 9.5px; }
</style>
</head>
<body>

  <div class="label" style="left:294px; top:52px;">Letterhead</div>
  <section class="letterhead">
    <div class="letterhead__name">Lakemont Kenbu Kai Karate Studio</div>
    <div class="letterhead__rule"></div>
    <div class="letterhead__contact">
      <b>Maplecrest Plaza</b><span class="dot"></span>38214 US Hwy. 61<span class="dot"></span>Cedar Hollow, Florida. 33812<span class="dot"></span><b>352-555-0183</b>
    </div>
    <div class="letterhead__mark">
      <div class="ring"></div>
      <div class="mark-text">LAKEMONT KENBU KAI KARATE</div>
    </div>
    <div class="letterhead__email">Lakemontkenbukaistudio@samplemail.net</div>
  </section>

  <div class="label" style="left:866px; top:108px;">Envelope</div>
  <section class="envelope-front">
    <div class="envelope-front__band"></div>
    <div class="envelope-front__return">
      <div class="studio">Lakemont Kenbu Kai Karate Studio</div>
      <div>Maplecrest Plaza</div>
      <div>38214 U.S. Hwy 61</div>
      <div>Cedar Hollow, Florida 33812</div>
    </div>
    <div class="envelope-front__mark">
      <div class="ring"></div>
      <div class="mark-text">LAKEMONT KENBU KAI KARATE</div>
    </div>
  </section>
  <div class="label" style="left:857px; top:452px;">Front</div>

  <section class="envelope-back">
    <svg width="542" height="271" viewBox="0 0 542 271">
      <rect x="0" y="0" width="542" height="271" fill="var(--gold)"/>
      <polygon points="0,0 542,0 542,4 440,88 102,88 0,4" fill="var(--black)"/>
      <line x1="4" y1="8" x2="538" y2="8" stroke="var(--grey-band)" stroke-width="3"/>
      <line x1="36" y1="32" x2="506" y2="32" stroke="var(--grey-band)" stroke-width="3"/>
      <line x1="68" y1="58" x2="474" y2="58" stroke="var(--grey-band)" stroke-width="3"/>
      <line x1="102" y1="88" x2="15" y2="255" stroke="#8a7a20" stroke-width="0.7"/>
      <line x1="440" y1="88" x2="527" y2="255" stroke="#8a7a20" stroke-width="0.7"/>
      <circle cx="271" cy="50" r="35" fill="var(--red)"/>
    </svg>
  </section>
  <div class="label" style="left:871px; top:795px;">Back</div>

  <div class="label" style="left:589px; top:864px;">Business Card</div>
  <section class="card card--front">
    <div class="card__brand">
      <div class="ring"></div>
      <div class="brand-name">Lakemont Kenbu Kai Karate Studio</div>
    </div>
    <div class="card__person">
      <div class="name">Sensei Marcus T. Ellery</div>
      <div class="role">Instructor</div>
    </div>
    <div class="card__address">
      <div class="plaza">Maplecrest Plaza</div>
      <div>38214 U.S. Hwy 61</div>
      <div>Cedar Hollow, Florida. 33812</div>
      <div class="phone">Phone: 352-555-0183</div>
    </div>
    <div class="card__email">Email:Lakemontkenbukaistudio@samplemail.net</div>
  </section>
  <div class="label" style="left:405px; top:1116px;">Front</div>

  <section class="card card--back">
    <div class="card__brand">
      <div class="ring"></div>
      <div class="brand-name">Lakemont Kenbu Kai Karate Studio</div>
    </div>
  </section>
  <div class="label" style="left:773px; top:1112px;">Back</div>

</body>
</html>
```